Single Sided Happy Hour Flyer Design

Create an entertaining business generating happy hour flyer to kick off a very important conference.

Needs to be a single sided, one page, email friendly design.

Industry/Entity Type

Apartment

Font styles to use
Sans Serif

Requirements
Must have
• Our company logo, location of happy hour, dress code instructions. Redfield Housing Council logo.
Nice to have
• dynamic design.
Should not have
• copyrighted images we do not have rights to.

```html
<!DOCTYPE html>
<html lang="en">
<head>
<meta charset="utf-8">
<title>Kickoff Happy Hour Flyer</title>
<link rel="stylesheet" href="https://fonts.googleapis.com/css2?family=Montserrat:wght@400;600;700;800;900&family=Monoton&display=swap">
<style>
  :root {
    --navy-deep: #0a1434;
    --navy: #1a2a66;
    --violet: #4a2a6e;
    --ember: #c8401c;
    --amber: #f39a1e;
    --orange: #f26a1b;
    --neon-red: #ff3b3b;
    --neon-glow: #ff7a5a;
    --white: #ffffff;
    --soft-white: #e8ecf5;
    --badge-red: #c8321e;
  }
  * { margin: 0; padding: 0; box-sizing: border-box; }
  html, body {
    width: 816px; height: 1200px; overflow: hidden;
    background: var(--navy-deep);
  }
  .flyer {
    position: relative;
    width: 816px; height: 1200px;
    overflow: hidden;
    font-family: "Montserrat", sans-serif;
    color: var(--white);
    text-align: center;
    background:
      radial-gradient(circle at 78% 48%, rgba(242,106,27,0.75) 0, rgba(200,64,28,0.45) 22%, transparent 48%),
      radial-gradient(circle at 20% 60%, rgba(74,42,110,0.7) 0, transparent 45%),
      radial-gradient(circle at 85% 15%, rgba(243,154,30,0.35) 0, transparent 30%),
      radial-gradient(circle at 12% 92%, rgba(120,150,230,0.25) 0, transparent 30%),
      linear-gradient(180deg, var(--navy) 0%, var(--navy-deep) 55%, #141a45 100%);
  }
  .brand {
    position: absolute; top: 52px; left: 0; right: 0;
    display: flex; flex-direction: column; align-items: center; gap: 12px;
  }
  .brand-square {
    width: 58px; height: 58px;
    background: #3d5bb8;
  }
  .brand-name {
    font-weight: 700; font-size: 20px; letter-spacing: 2px;
    color: var(--soft-white); text-transform: uppercase;
  }
  .presents {
    position: absolute; top: 220px; left: 0; right: 0;
    font-weight: 800; font-size: 30px; letter-spacing: 1px;
    color: var(--amber);
  }
  .event-title {
    position: absolute; top: 260px; left: 0; right: 0;
    font-weight: 800; font-size: 38px; letter-spacing: 1px;
  }
  .neon-headline {
    position: absolute; top: 345px; left: 0; right: 0;
    font-family: "Monoton", sans-serif;
    color: var(--white);
    line-height: 1;
    text-shadow: 0 0 8px var(--neon-red), 0 0 18px var(--neon-red), 0 0 36px var(--neon-glow);
  }
  .neon-happy { display: block; font-size: 140px; margin-left: 60px; }
  .neon-hour { display: block; font-size: 130px; margin-top: 24px; margin-left: 170px; }
  .champagne {
    position: absolute; left: 60px; top: 480px;
    width: 110px; height: 190px;
    border-radius: 50% 50% 10px 10px;
    background: linear-gradient(180deg, rgba(255,220,140,0.85), rgba(200,140,50,0.55) 60%, rgba(255,255,255,0.25));
  }
  .invite {
    position: absolute; top: 770px; left: 0; right: 0;
    font-size: 24px; font-weight: 400; line-height: 1.35;
    color: var(--soft-white);
  }
  .detail-label {
    position: absolute; left: 0; right: 0;
    font-weight: 800; font-size: 28px; color: var(--amber);
  }
  .label-location { top: 880px; }
  .label-date { top: 990px; }
  .address {
    position: absolute; top: 922px; left: 0; right: 0;
    font-weight: 700; font-size: 24px;
  }
  .date {
    position: absolute; top: 1030px; left: 0; right: 0;
    font-weight: 900; font-size: 42px; letter-spacing: 1px;
  }
  .time {
    position: absolute; top: 1088px; left: 0; right: 0;
    font-weight: 800; font-size: 34px; color: var(--orange);
  }
  .partner {
    position: absolute; left: 40px; bottom: 40px;
    display: flex; align-items: center; gap: 10px;
    background: var(--white);
    padding: 10px 14px;
  }
  .partner-square { width: 26px; height: 26px; background: var(--badge-red); }
  .partner-name {
    font-weight: 700; font-size: 13px; color: var(--navy);
    text-align: left; width: 120px; line-height: 1.2;
  }
  .dress-badge {
    position: absolute; right: 24px; bottom: 22px;
    width: 96px; height: 96px; border-radius: 50%;
    background: var(--badge-red);
    border: 3px solid rgba(255,255,255,0.35);
    display: flex; align-items: center; justify-content: center;
    font-weight: 800; font-size: 17px; line-height: 1.15;
  }
</style>
</head>
<body>
  <main class="flyer">
    <header class="brand">
      <div class="brand-square"></div>
      <div class="brand-name">Bastion Builders</div>
    </header>

    <p class="presents">PROUDLY PRESENTS</p>
    <h1 class="event-title">KICKOFF HAPPY 2 HOUR</h1>

    <div class="neon-headline" aria-label="Happy Hour">
      <span class="neon-happy">Happy</span>
      <span class="neon-hour">Hour</span>
    </div>

    <div class="champagne" role="img" aria-label="Two clinking champagne glasses"></div>

    <p class="invite">Bastion Builders Cordially<br>Invites You To Join Us For Cocktails And Hors D'oeuvers</p>

    <p class="detail-label label-location">LOCATION</p>
    <p class="address">HARBORLINE BAR AND GRILL RIGHT NEXT TO LOBBY BAR</p>

    <p class="detail-label label-date">DATE &amp; TIME</p>
    <p class="date">WEDNESDAY 10TH APRIL</p>
    <p class="time">5:30 TILL 7:30</p>

    <div class="partner">
      <div class="partner-square"></div>
      <div class="partner-name">Redfield Housing Council</div>
    </div>

    <div class="dress-badge">CASUAL<br>DRESS</div>
  </main>
</body>
</html>
```